Simple, Professional and neat business card design for Vellamor Inc.

We're looking to re-vamp our business card design. We're a supplier of innovative feed ingredients for the North American animal agriculture industry. We are located in Lucknow, Ontario, Canada and our flagship product is a product that prevents milk fever in dairy cows when the calve, it is fed before calving and is very effective compared to other alternatives available on the market today.

Our company has Danish roots and we import all of our product from our Danish partner/manufacturer in Denmark. We like our design to embrace high professionalism while remaining neat and simple.

Target Market(s)

B2B, Feed Mills, Veterinary Clinics, Large integrators/producers,

Industry/Entity Type

Agribusiness

Contact Information for Business Card

We like the rounded corners because they make the card easy to sit in a wallet and not many use it so it makes the card stand out, just possibly something to take account for during the design.

As you can also see on the sliders below, looking for a that simple but proffesional scandinavian design.

Requirements
Nice to have
• Rounded corners
Should not have
• Too vibrant

```html
<!DOCTYPE html>
<html lang="en">
<head>
<meta charset="utf-8">
<title>Vellamor Inc. business card</title>
<link href="https://fonts.googleapis.com/css2?family=Open+Sans:wght@400;600;700;800&display=swap" rel="stylesheet">
<style>
  :root {
    --page: #e9eaec;
    --brand-blue: #0f4fa0;
    --brand-blue-deep: #0a3b7e;
    --brand-blue-light: #1d63bd;
    --card-white: #f7f6f3;
    --ray-tint: #ebe4d6;
    --ink: #3c3c3c;
    --rule: #6b6b6b;
    --white: #ffffff;
  }
  * { box-sizing: border-box; margin: 0; padding: 0; }
  html, body { width: 1200px; height: 960px; overflow: hidden; }
  body {
    background: var(--page);
    font-family: "Open Sans", Arial, sans-serif;
    position: relative;
  }
  .card {
    position: absolute;
    left: 220px;
    width: 760px;
    height: 434px;
    border-radius: 34px;
    overflow: hidden;
    box-shadow: 0 10px 30px rgba(0,0,0,0.18);
  }
  /* back side */
  .card-back {
    top: 30px;
    background: radial-gradient(ellipse at 50% 40%, var(--brand-blue-light) 0%, var(--brand-blue) 55%, var(--brand-blue-deep) 100%);
  }
  .back-mark {
    position: absolute;
    left: 0; right: 0; top: 160px;
    display: flex; align-items: center; justify-content: center; gap: 16px;
  }
  .back-mark .mark-square {
    width: 34px; height: 34px; background: var(--white);
  }
  .back-mark .mark-name {
    font-weight: 800; font-size: 46px; color: var(--white); letter-spacing: 1px;
  }
  .tagline {
    position: absolute;
    left: 0; right: 0; bottom: 40px;
    text-align: center;
    color: var(--white);
    font-weight: 600;
    font-size: 22px;
  }
  /* front side */
  .card-front {
    top: 496px;
    background: var(--card-white);
  }
  .ray-field {
    position: absolute; inset: 0;
    background: radial-gradient(ellipse at 38% 100%, var(--ray-tint) 0%, var(--card-white) 70%);
  }
  .front-mark {
    position: absolute; right: 50px; top: 60px;
    display: flex; align-items: center; gap: 14px;
  }
  .front-mark .mark-square { width: 36px; height: 36px; background: var(--brand-blue); }
  .front-mark .mark-name {
    font-weight: 800; font-size: 42px; color: var(--brand-blue);
  }
  .person-name {
    position: absolute; left: 50px; top: 104px;
    font-weight: 700; font-size: 26px; color: var(--brand-blue);
  }
  .divider {
    position: absolute; left: 50px; right: 50px; top: 152px;
    height: 1px; background: var(--rule);
  }
  .contact-list {
    position: absolute; left: 50px; top: 168px;
    list-style: none;
  }
  .contact-list li {
    display: flex; align-items: center; gap: 12px;
    font-size: 21px; line-height: 31px; color: var(--ink);
  }
  .contact-list svg { width: 22px; height: 22px; fill: var(--brand-blue); flex: none; }
  .address {
    position: absolute; right: 50px; bottom: 42px;
    text-align: right; color: var(--ink);
    font-size: 23px; line-height: 30px;
  }
  .address .web { letter-spacing: 4px; }
</style>
</head>
<body>
  <section class="card card-back">
    <div class="back-mark">
      <span class="mark-square"></span>
      <span class="mark-name">Vellamor Inc.</span>
    </div>
    <p class="tagline">Protecting the health of your animals</p>
  </section>

  <section class="card card-front">
    <div class="ray-field" role="img" aria-label="Soft sunburst rays in pale beige radiating across the card"></div>
    <div class="front-mark">
      <span class="mark-square"></span>
      <span class="mark-name">VELLAMOR INC.</span>
    </div>
    <h1 class="person-name">ANDERS HOLMVIK</h1>
    <div class="divider"></div>
    <ul class="contact-list">
      <li><svg viewBox="0 0 24 24"><path d="M6.6 10.8a15.1 15.1 0 0 0 6.6 6.6l2.2-2.2c.3-.3.7-.4 1-.2 1.1.4 2.3.6 3.6.6.6 0 1 .4 1 1V20c0 .6-.4 1-1 1A17 17 0 0 1 3 4c0-.6.4-1 1-1h3.5c.6 0 1 .4 1 1 0 1.3.2 2.5.6 3.6.1.3 0 .7-.2 1z"/></svg>888-604-2917 (TF)</li>
      <li><svg viewBox="0 0 24 24"><path d="M6.6 10.8a15.1 15.1 0 0 0 6.6 6.6l2.2-2.2c.3-.3.7-.4 1-.2 1.1.4 2.3.6 3.6.6.6 0 1 .4 1 1V20c0 .6-.4 1-1 1A17 17 0 0 1 3 4c0-.6.4-1 1-1h3.5c.6 0 1 .4 1 1 0 1.3.2 2.5.6 3.6.1.3 0 .7-.2 1z"/></svg>519-730-4418</li>
      <li><svg viewBox="0 0 24 24"><path d="M7 1h10a2 2 0 0 1 2 2v18a2 2 0 0 1-2 2H7a2 2 0 0 1-2-2V3a2 2 0 0 1 2-2zm0 3v14h10V4z"/></svg>519-730-6621</li>
      <li><svg viewBox="0 0 24 24"><path d="M6 2h9l3 3v4h1a3 3 0 0 1 3 3v7h-4v3H6v-3H2v-7a3 3 0 0 1 3-3h1zm2 2v5h8V6h-2V4zm0 11v5h8v-5z"/></svg>519-730-4490</li>
      <li><svg viewBox="0 0 24 24"><path d="M2 5h20v14H2zm2 2v.5l8 5 8-5V7l-8 5z"/></svg>anders@vellamor.com</li>
    </ul>
    <address class="address">
      Box 412, Carrow<br>
      Ontario Canada N0X 4K1<br>
      <span class="web">www.vellamor.com</span>
    </address>
  </section>
</body>
</html>
```